Dermavive Label Design

We need a label design for our cream dispenser. Its a cream against acne called Dermavive, Works with its active ingredients of silver and oxygen. We are looking for a flashy / colorful and modern design .
Updates

Low design quality

Target Market(s)

young people / People with acne

Industry/Entity Type

Skin Care Product

Colors

Designer to choose colors to be used in the design.

Requirements
Must have
• be modern, Colours
• -THE DESIGN NEEDS TO BE 10,7x7 , ITS 1 BIG STICKER THAT RAPS AROUND THE BOTTLE

```html
<!DOCTYPE html>
<html lang="en">
<head>
<meta charset="utf-8">
<title>Dermavive Acne Repair &amp; Care Label</title>
<link rel="stylesheet" href="https://fonts.googleapis.com/css2?family=Hind:wght@400;500&family=Josefin+Sans:wght@600;700&family=Quicksand:wght@600;700&family=Lato:wght@700&display=swap">
<style>
  :root {
    --teal: #22bcc4;
    --teal-soft: #8fd4d4;
    --teal-line: #4aa9ae;
    --ink: #2f3236;
    --ice: #dcf0f4;
    --paper: #ffffff;
    --backdrop: #e9ecee;
  }
  * { box-sizing: border-box; margin: 0; padding: 0; }
  html, body {
    width: 1200px; height: 850px; overflow: hidden;
    background: var(--backdrop);
  }
  .label {
    position: absolute; left: 55px; top: 68px;
    width: 1090px; height: 713px;
    background: var(--paper);
    box-shadow: 0 4px 14px rgba(0,0,0,.25);
    overflow: hidden;
    font-family: "Hind", sans-serif;
    color: var(--ink);
  }
  .label__backdrop { position: absolute; inset: 0; }
  .tab {
    position: absolute; height: 39px; width: 183px;
    background: var(--teal); color: #fff;
    border-radius: 0 16px 0 0;
    font-family: "Hind", sans-serif; font-weight: 500;
    font-size: 21px; line-height: 42px; padding-left: 10px;
  }
  .copy {
    position: absolute; font-size: 21px; line-height: 26px;
  }
  .copy--caps { text-transform: uppercase; }
  .brand-mark {
    position: absolute; left: 480px; top: 57px;
    width: 130px; height: 48px;
    border: 2px solid var(--ink); border-radius: 4px;
    font-family: "Hind", sans-serif; font-weight: 500;
    font-size: 22px; line-height: 50px; text-align: center;
    color: var(--ink);
  }
  .brand-name {
    position: absolute; left: 363px; width: 363px; top: 113px;
    text-align: center;
    font-family: "Quicksand", sans-serif; font-weight: 700;
    font-size: 42px; letter-spacing: 5px; color: var(--teal);
  }
  .product-title {
    position: absolute; left: 363px; width: 363px; top: 330px;
    text-align: center; color: #fff;
    font-family: "Josefin Sans", sans-serif; font-weight: 700;
    font-size: 66px; line-height: 66px; letter-spacing: -1px;
  }
  .volume {
    position: absolute; left: 497px; top: 624px;
    width: 96px; height: 45px;
    border: 2px solid #fff; border-radius: 3px;
    color: #fff; font-family: "Quicksand", sans-serif; font-weight: 700;
    font-size: 20px; line-height: 42px; text-align: center;
  }
  .maker-mark {
    position: absolute; left: 250px; top: 624px;
    display: flex; align-items: center; gap: 6px;
    font-family: "Hind", sans-serif; font-weight: 500; font-size: 22px;
  }
  .maker-mark__square { width: 12px; height: 12px; background: var(--ink); }
  .origin-badge {
    position: absolute; left: 818px; top: 492px;
    width: 180px; height: 130px; border-radius: 6px;
    background: linear-gradient(180deg, #2b2b2b 0%, #2b2b2b 30%, #d42a1f 33%, #d42a1f 63%, #f1c40f 66%, #f1c40f 100%);
  }
  .origin-text {
    position: absolute; left: 726px; width: 364px; top: 642px;
    text-align: center; font-family: "Quicksand", sans-serif;
    font-weight: 700; font-size: 23px; color: var(--ink);
  }
</style>
</head>
<body>
<main class="label">
  <svg class="label__backdrop" width="1090" height="713" viewBox="0 0 1090 713" aria-hidden="true">
    <defs>
      <linearGradient id="tealPanel" x1="0" y1="0" x2="0" y2="1">
        <stop offset="0" stop-color="#8fd6d6"/>
        <stop offset="1" stop-color="#22bcc4"/>
      </linearGradient>
      <linearGradient id="iceFade" x1="0" y1="0" x2="0" y2="1">
        <stop offset="0" stop-color="#e8f5f7"/>
        <stop offset="1" stop-color="#d6eef2"/>
      </linearGradient>
    </defs>
    <path d="M0,270 Q170,195 363,200 L363,713 L0,713 Z" fill="url(#iceFade)"/>
    <path d="M363,200 Q570,212 726,290 L726,713 L363,713 Z" fill="url(#tealPanel)"/>
    <path d="M726,290 Q930,390 1090,555 L1090,713 L726,713 Z" fill="url(#iceFade)"/>
    <g fill="none" stroke-linecap="round">
      <path d="M0,262 Q180,186 363,192 Q580,204 740,282 Q935,380 1090,545" stroke="#ffffff" stroke-width="5"/>
      <path d="M363,196 Q575,208 732,286" stroke="var(--teal-line)" stroke-width="4"/>
      <path d="M363,210 Q575,222 726,298" stroke="var(--teal-line)" stroke-width="3" opacity=".8"/>
      <path d="M363,222 Q565,236 726,308" stroke="var(--teal-line)" stroke-width="2" opacity=".6"/>
      <path d="M0,280 Q160,215 363,214" stroke="#c9e6ec" stroke-width="2"/>
      <path d="M726,300 Q930,400 1090,570" stroke="#c9e6ec" stroke-width="2"/>
    </g>
  </svg>

  <div class="tab" style="left:19px;top:37px;">USAGE:</div>
  <p class="copy" style="left:29px;top:94px;width:320px;">Apply 2 times daily on dry clean skin, Do not combine with any other products. Do not use harsh Cleaning products.</p>

  <div class="tab" style="left:19px;top:216px;">WARNING:</div>
  <p class="copy" style="left:29px;top:276px;width:300px;">For external use only. Avoid contact with eyes.</p>

  <div class="tab" style="left:19px;top:349px;">Distributed by</div>
  <p class="copy copy--caps" style="left:29px;top:410px;width:320px;">Dermavive LLC<br>48 Linden Hollow<br>Rd Suite 12<br>Harborview, PA 15090</p>

  <div class="tab" style="left:19px;top:534px;">Manufactured By</div>
  <p class="copy" style="left:29px;top:596px;width:240px;"><span style="text-transform:uppercase">KL Skin Labs</span><br>Birkenweg 7, 40210<br>Aldenfeld Distributer</p>
  <div class="maker-mark"><span class="maker-mark__square"></span>KL</div>

  <div class="brand-mark">Novora AG</div>
  <div class="brand-name">Dermavive</div>

  <h1 class="product-title">ACNE<br>REPAIR<br>&amp; CARE</h1>
  <div class="volume">50ml</div>

  <div class="tab" style="left:744px;top:37px;">INGREDIENTS:</div>
  <p class="copy" style="left:751px;top:94px;width:325px;">Aquar (Water), Petolatum, Propylene Glycol, Caprylic/capric Triglyceride, PEG-20 Glyceryl Stearate, Cetearyl Alcohol, OenotheraBiennis (Evening Primrose) Oil, Glyceryl Stearate, Aloe Barbadensis Leaf Juice, Calendula Officinalis Flower Extract, Sodium Citrate, Xanthan Gum, Hydrogen Peroxide, Silver Citrate, Parfum (Fragrance)</p>

  <div class="origin-badge" role="img" aria-label="Waving German flag badge marking the product as made in Germany"></div>
  <p class="origin-text">Made In Germany</p>
</main>
</body>
</html>
```